Vorin Co Premium Matcha brand Label

This is a label design project for a luxury tea brand. Feel free to be creative within the guidelines.
Attached to this project is a document called “Private Label Design Requirements” with the design guidelines and template. There is another document called "Vorin Co Packaging Instructions" this has more details necessary to stick to the guidelines in the first document.

I have also attached the certifications to be included as well as different variations of the logo for you to use.

If you have any questions, I am here.

Need extra days to review

Young, active, fun, enjoy the finer things

```html
<!DOCTYPE html>
<html lang="en">
<head>
<meta charset="utf-8">
<title>Vorin Co Premium Matcha Labels</title>
<link href="https://fonts.googleapis.com/css2?family=Barlow:wght@400;600;700&family=Montserrat:wght@600&family=Oswald:wght@500&display=swap" rel="stylesheet">
<style>
  :root {
    --bg: #e6e6e6;
    --ink: #1b1b1b;
    --green: #5cbf44;
    --green-deep: #3f9a2e;
    --leaf-pale: #e3efdb;
    --white: #ffffff;
    --badge-ring: #2f7d3a;
  }
  * { box-sizing: border-box; margin: 0; padding: 0; }
  html, body { width: 1200px; height: 710px; overflow: hidden; background: var(--bg); }
  body { position: relative; font-family: "Barlow", sans-serif; }

  .label { position: absolute; left: 40px; width: 1120px; height: 188px; border-radius: 14px; overflow: hidden; }
  .label--classic { top: 95px; background: var(--ink); color: var(--white); }
  .label--bold { top: 420px; background: var(--green); color: var(--ink); }

  .abs { position: absolute; }

  /* badges */
  .badge-square { width: 58px; height: 58px; background: var(--white); border: 3px solid var(--green-deep); border-radius: 4px; }
  .badge-circle { width: 54px; height: 54px; border-radius: 50%; background: var(--white); border: 5px solid var(--badge-ring); }

  .distributor { font-size: 12.5px; line-height: 16px; }

  /* classic label */
  .dot-band { left: 0; top: 0; width: 100%; height: 28px; background: var(--green); }
  .dot-rule { top: 165px; height: 0; border-top: 4px dotted var(--green); }
  .ribbon { top: 72px; height: 40px; background: var(--green); color: var(--ink);
    font-family: "Montserrat", sans-serif; font-weight: 600; font-size: 22px; letter-spacing: 1px;
    display: flex; align-items: center; justify-content: center;
    clip-path: polygon(0 0, 100% 0, 94% 50%, 100% 100%, 0 100%, 6% 50%); }
  .brand-name { font-family: "Barlow", sans-serif; font-weight: 700; font-size: 21px; display: flex; align-items: center; gap: 7px; }
  .brand-dot { width: 12px; height: 12px; border-radius: 50%; background: var(--green); }
  .net-weight { font-size: 11.5px; font-weight: 700; letter-spacing: .4px; white-space: nowrap; }

  .facts { font-size: 11.5px; line-height: 14px; }
  .facts h3 { font-size: 11.5px; font-weight: 700; text-transform: uppercase; }
  .facts ul { list-style: none; margin-bottom: 6px; }
  .facts li::before { content: ""; display: inline-block; width: 6px; height: 6px; border-radius: 50%; background: var(--green); margin-right: 5px; vertical-align: 1px; }
  .facts .notice { font-weight: 700; text-transform: uppercase; }
  .facts p { margin-bottom: 6px; }

  /* bold label */
  .dark-band { left: 0; top: 18px; width: 100%; height: 82px; background: var(--ink); }
  .dark-foot { left: 0; bottom: 0; width: 100%; height: 14px; background: var(--ink); }
  .brand-panel { left: 350px; top: 0; width: 172px; height: 170px; background: var(--leaf-pale);
    clip-path: polygon(0 0, 100% 0, 100% 90%, 50% 100%, 0 90%); }
  .brand-panel .brand-name { position: absolute; left: 0; right: 0; top: 112px; justify-content: center; color: var(--ink); }
  .brand-panel .brand-dot { background: var(--green-deep); }
  .headline-line { left: 540px; font-family: "Oswald", sans-serif; font-weight: 500; font-size: 60px; line-height: 60px; letter-spacing: -1px; white-space: nowrap; transform: scaleY(1.15); transform-origin: top left; }
  .headline-line--top { top: 24px; color: var(--green); }
  .headline-line--bottom { top: 88px; color: var(--ink); }
  .label--bold .facts li::before { background: var(--ink); }
  .facts--compact { line-height: 12.5px; font-size: 11px; }
  .facts--compact h3 { font-size: 11px; }
  .facts--compact ul { margin-bottom: 0; }
</style>
</head>
<body>

  <section class="label label--classic" aria-label="Classic black label">
    <div class="abs dot-band" role="img" aria-label="Green band with dot pattern"></div>
    <div class="abs badge-square" style="left:44px;top:44px" role="img" aria-label="Non-GMO certification badge"></div>
    <div class="abs badge-circle" style="left:112px;top:46px" role="img" aria-label="Organic certification badge"></div>
    <div class="abs distributor" style="left:44px;top:110px">
      Distributed by Vorin Co | Larkfield, Ga<br>Certified Organic by Velden<br>Product of Japan
    </div>

    <div class="abs ribbon" style="left:318px;width:168px">PREMIUM</div>
    <div class="abs brand-name" style="left:500px;top:112px"><span class="brand-dot"></span>Vorin Co</div>
    <div class="abs ribbon" style="left:632px;width:168px">MATCHA</div>
    <div class="abs net-weight" style="left:498px;top:152px">Net Wt: 30g (1.06oz)</div>

    <div class="abs dot-rule" style="left:10px;width:472px"></div>
    <div class="abs dot-rule" style="left:640px;width:470px"></div>

    <div class="abs facts" style="left:836px;top:36px">
      <h3>Ingredients:</h3>
      <p>Premium Organic Japanese Matcha Green Tea</p>
      <h3>Instructions:</h3>
      <ul>
        <li>2 tsp of Matcha</li>
        <li>2oz of Water (170-180 degrees F)</li>
        <li>Whisk in a W formation until frothy</li>
        <li>Sweeten to taste</li>
      </ul>
      <div class="notice">Keep refrigerated for quality</div>
    </div>
  </section>

  <section class="label label--bold" aria-label="Bold green label">
    <div class="abs dark-band"></div>
    <div class="abs dark-foot"></div>
    <div class="abs badge-square" style="left:44px;top:30px" role="img" aria-label="Non-GMO certification badge"></div>
    <div class="abs badge-circle" style="left:112px;top:32px" role="img" aria-label="Organic certification badge"></div>
    <div class="abs distributor" style="left:44px;top:122px">
      Distributed by Vorin Co | Larkfield, Ga<br>Certified Organic by Velden<br>Product of Japan
    </div>

    <div class="abs brand-panel">
      <div class="brand-name"><span class="brand-dot"></span>Vorin Co</div>
    </div>
    <div class="abs headline-line headline-line--top">PREMIUM</div>
    <div class="abs headline-line headline-line--bottom">MATCHA</div>
    <div class="abs net-weight" style="left:540px;top:158px">Net Wt: 30g (1.06oz)</div>

    <div class="abs facts" style="left:840px;top:34px;color:var(--white)">
      <h3>Ingredients:</h3>
      <p>Premium Organic Japanese Matcha Green Tea</p>
      <div class="notice">Keep refrigerated for quality</div>
    </div>
    <div class="abs facts facts--compact" style="left:840px;top:108px">
      <h3>Instructions:</h3>
      <ul>
        <li>2 tsp of Matcha</li>
        <li>2oz of Water (170-180 degrees F)</li>
        <li>Whisk in a W formation until frothy</li>
        <li>Sweeten to taste</li>
      </ul>
    </div>
  </section>

</body>
</html>
```